We want to revamp our current website -www.kelvoro-tek.com

We need to have a new website for our company that offers non-destructive and testing solutions around Africa. We have a current website but it does not fulfil our needs as it is:<br/>1. Not clear and bright<br/>2. Does not fit well in mobile <br/>3. Is not easily updatable by our staff. <br/>4. Is not linked to our social media sites.<br/>We would like to have a website that addresses the above issues. Our colours are Red and Blue and should communicate to our clients, that we are a professional company open for business, ready to solve their non-destructive testing problems around Africa. * Helpful if it is a wordpress website.

Target Market(s)

Our customers are B2B Corporate clients. We mainly work in
1. Storage Terminals
2. Refineries
3. Oil and Gas offshore and onshore rigs.

Industry/Entity Type

Oil And Gas

Contact Information for Business Card

Please find our current business card on the uploaded files.

Coding

Coded - Design and coding required

Number of Pages Required

5+ page

Font styles to use
Serif
Sans Serif

Requirements
Must have
• I like this site www.pirel-checkworks.com They are in the same industry.
• I don't understand how to call them but all the 'call to action' buttons, and links to our Social media pages.
• Must have a place where we update information in a regular basis. A Blog!

```html
<!DOCTYPE html>
<html lang="en">
<head>
<meta charset="utf-8">
<title>Kelvoro Tek — Inspection &amp; Engineering Services</title>
<link rel="stylesheet" href="https://fonts.googleapis.com/css2?family=Anton&family=Lato:wght@400;700&family=Ubuntu:wght@400;500&display=swap">
<style>
:root{
  --navy:#25346e;
  --navy-deep:#1f2c5f;
  --red:#b0161b;
  --red-soft:#c0282c;
  --gray:#eceef2;
  --ink:#333;
  --muted:#555;
  --white:#fff;
}
*{margin:0;padding:0;box-sizing:border-box}
html,body{width:1200px;height:3479px;overflow:hidden;background:var(--white)}
body{position:relative;font-family:"Lato",sans-serif;color:var(--ink)}
.abs{position:absolute}
a{text-decoration:none;color:inherit}

/* backgrounds */
.bg-gray{background:var(--gray)}
.bg-navy{background:linear-gradient(135deg,#2b3b78,#22306a 60%,#1e2b60)}

/* header */
.brand{left:77px;top:30px;display:flex;align-items:center;gap:10px;font-family:"Ubuntu",sans-serif;font-weight:500;font-size:26px;color:var(--navy)}
.brand .dot{width:36px;height:36px;border-radius:50%;background:var(--red)}
.nav{top:40px;left:0;font-size:15px;font-family:"Lato",sans-serif}
.nav a{position:absolute;white-space:nowrap;color:#222}
.nav a.on-dark{color:var(--white)}
.nav a.active{color:var(--red)}
.nav a.active::after{content:"";position:absolute;left:0;right:0;bottom:-6px;height:2px;background:var(--red)}

/* hero */
.hero-title{left:709px;top:222px;font-family:"Anton",sans-serif;font-size:62px;line-height:64px;color:var(--white);letter-spacing:1px}
.hero-sub{left:712px;top:364px;font-size:19px;color:var(--white)}
.btn{display:flex;align-items:center;justify-content:center;background:var(--red);color:var(--white);font-family:"Ubuntu",sans-serif;font-weight:500;font-size:19px;border-radius:3px;box-shadow:0 3px 8px rgba(0,0,0,.2)}
.photo{border:0}

/* services */
.eyebrow{font-family:"Ubuntu",sans-serif;font-size:20px;color:var(--red)}
.h2{font-family:"Ubuntu",sans-serif;font-weight:500;font-size:42px;color:var(--navy)}
.service{width:260px}
.service .icon{position:relative;width:110px;height:105px}
.service .icon .blob{position:absolute;left:0;top:0;width:62px;height:62px;border-radius:50%;background:var(--red)}
.service .icon svg{position:absolute;left:18px;top:10px}
.service h3{font-family:"Ubuntu",sans-serif;font-weight:500;font-size:22px;color:var(--navy);margin-top:36px}
.service p{font-size:15px;line-height:27px;color:#444;margin-top:16px}
.service .more{display:inline-flex;align-items:center;gap:6px;margin-top:20px;font-size:18px;color:var(--red)}
.service .more::after{content:"";border-left:8px solid var(--red);border-top:6px solid transparent;border-bottom:6px solid transparent}

/* welcome */
.welcome-kicker{left:669px;top:1358px;font-family:"Ubuntu",sans-serif;font-size:21px;color:var(--white)}
.welcome-title{left:669px;top:1390px;font-family:"Ubuntu",sans-serif;font-weight:500;font-size:44px;letter-spacing:1px;color:var(--white)}
.welcome-copy{left:671px;top:1456px;width:420px;font-size:14px;line-height:27px;color:var(--white)}
.welcome-copy p+p{margin-top:10px}

/* inspection */
.center{text-align:center}
.insp-title{left:0;width:1200px;top:2288px;font-family:"Ubuntu",sans-serif;font-weight:500;font-size:21px;line-height:29px;color:var(--navy)}
.insp-copy{left:290px;width:620px;top:2357px;font-size:14.5px;line-height:27px;color:var(--muted)}
.chev{width:26px;height:44px}

/* blog */
.blog-kicker{left:76px;top:2644px;font-family:"Ubuntu",sans-serif;font-size:20px;color:#7a1a2a}
.blog-title{left:73px;top:2680px;font-family:"Ubuntu",sans-serif;font-weight:500;font-size:44px;color:var(--white)}
.post-date{left:234px;top:2772px;font-size:16px;color:#8a1d2a}
.post-title{left:234px;top:2807px;font-family:"Ubuntu",sans-serif;font-weight:500;font-size:17px;line-height:27px;color:var(--white)}
.post-copy{left:234px;top:2875px;width:400px;font-size:14px;line-height:27px;color:#d6daea}
.round{width:46px;height:46px;border-radius:50%;display:flex;align-items:center;justify-content:center}
.round.fill{background:var(--red)}
.round.line{border:1.5px solid var(--red)}

/* footer */
.f-head{font-family:"Ubuntu",sans-serif;font-weight:500;font-size:18px;color:var(--navy)}
.sitemap{list-style:none;font-size:15px;color:#444}
.sitemap li{position:relative;padding-left:19px;height:29px}
.sitemap li::before{content:"";position:absolute;left:0;top:7px;width:5px;height:5px;border-radius:50%;background:var(--red)}
.contact-row{display:flex;gap:18px;font-size:14px;line-height:24px;color:#555}
.contact-row svg{flex:none;margin-top:2px}
.news-copy{font-size:15px;line-height:26px;color:#555;width:245px}
.email-field{border:1px solid #ddd;background:#f7f7f7;font-size:14px;color:#666;padding-left:14px;display:flex;align-items:center}
.social{width:48px;height:48px;border-radius:50%;background:var(--navy)}
.rule{left:77px;width:1046px;top:3418px;height:1px;background:#ddd}
.copyright{left:0;width:1200px;top:3440px;font-size:14px;color:#333}
</style>
</head>
<body>

<!-- background blocks -->
<div class="abs bg-gray" style="left:0;top:527px;width:501px;height:150px"></div>
<div class="abs bg-gray" style="left:0;top:676px;width:989px;height:598px"></div>
<div class="abs bg-gray" style="left:0;top:1274px;width:315px;height:243px"></div>
<div class="abs bg-navy" style="left:501px;top:0;width:699px;height:677px" role="img" aria-label="Technician in safety gear working on a pipeline, tinted blue"></div>
<div class="abs bg-navy" style="left:315px;top:1274px;width:885px;height:499px" role="img" aria-label="Industrial workers on site, tinted blue"></div>
<div class="abs bg-navy" style="left:0;top:2571px;width:989px;height:532px" role="img" aria-label="Industrial facility backdrop, tinted blue"></div>

<!-- header -->
<div class="abs brand"><span class="dot"></span>Kelvoro Tek</div>
<nav class="abs nav">
  <a class="active" style="left:365px">Home</a>
  <a style="left:432px">About Us</a>
  <a class="on-dark" style="left:516px">Inspection</a>
  <a class="on-dark" style="left:608px">NDT Services</a>
  <a class="on-dark" style="left:719px">Advance NDT Services</a>
  <a class="on-dark" style="left:892px">Engineering Services</a>
  <a class="on-dark" style="left:1048px">Contact Us</a>
</nav>

<!-- hero -->
<div class="abs photo" style="left:138px;top:345px;width:497px;height:332px;background:linear-gradient(135deg,#3a4450,#6f7680 40%,#a07a4a 75%,#3a2a20);border-right:4px solid var(--red)" role="img" aria-label="Hands operating an ultrasonic flaw detector with waveform display"></div>
<div class="abs hero-title">Kelvoro<br>Tek</div>
<div class="abs hero-sub">We offer inspection &amp; engineering services</div>
<a class="abs btn" style="left:717px;top:409px;width:177px;height:52px">CONTACT US</a>

<!-- services -->
<div class="abs eyebrow" style="left:152px;top:768px">What We Do</div>
<h2 class="abs h2" style="left:148px;top:800px">Services We Provide</h2>

<div class="abs service" style="left:143px;top:892px">
  <div class="icon"><span class="blob"></span>
    <svg width="90" height="90" viewBox="0 0 90 90" fill="none" stroke="#111" stroke-width="3"><circle cx="14" cy="14" r="8" fill="#fff"/><path d="M20 18 L58 36 L40 64 Z" fill="#fff"/><circle cx="62" cy="38" r="9" fill="#fff"/><circle cx="38" cy="68" r="13" fill="#fff"/><circle cx="38" cy="68" r="4"/></svg>
  </div>
  <h3 style="margin-top:28px">Engineering Services</h3>
  <p>Our Mechanical Engineering division is majorly involved with ASME com-pliant steel fabrication...</p>
  <a class="more">Read More</a>
</div>
<div class="abs service" style="left:428px;top:892px">
  <div class="icon"><span class="blob"></span>
    <svg width="90" height="90" viewBox="0 0 90 90" fill="none" stroke="#111" stroke-width="3"><rect x="8" y="6" width="74" height="62" rx="3" fill="#fff"/><line x1="8" y1="18" x2="82" y2="18"/><path d="M24 56 A21 21 0 0 1 66 56" /><line x1="45" y1="56" x2="56" y2="40"/><line x1="38" y1="68" x2="34" y2="80"/><line x1="52" y1="68" x2="56" y2="80"/><line x1="26" y1="80" x2="64" y2="80"/></svg>
  </div>
  <h3 style="margin-top:14px">NDT Services</h3>
  <p>Using the latest ultrasound techn -ology, we can verify the thickness of a material and ascertain....</p>
  <a class="more">Read More</a>
</div>
<div class="abs service" style="left:709px;top:892px">
  <div class="icon"><span class="blob"></span>
    <svg width="90" height="90" viewBox="0 0 90 90" fill="none" stroke="#111" stroke-width="3"><rect x="12" y="6" width="46" height="76" rx="4" fill="#fff"/><rect x="20" y="16" width="14" height="18"/><line x1="20" y1="42" x2="48" y2="42"/><line x1="20" y1="50" x2="48" y2="50"/><line x1="20" y1="58" x2="40" y2="58"/><path d="M52 44 L60 40 L80 60 L68 72 L54 62 Z" fill="#fff"/></svg>
  </div>
  <h3 style="margin-top:12px">Advance NDT Services</h3>
  <p>We are the first local company to introduce this technology. KELVORO utilises MFL technology...</p>
  <a class="more">Read More</a>
</div>

<!-- welcome -->
<div class="abs" style="left:77px;top:1359px;width:500px;height:333px;background:linear-gradient(135deg,#1c1e22,#4a4e55 45%,#6b8a3a 60%,#2a2d33)" role="img" aria-label="Magnetic particle yoke being used on a steel surface"></div>
<div class="abs welcome-kicker">Welcome To</div>
<div class="abs welcome-title">Kelvoro-tek</div>
<div class="abs welcome-copy">
  <p>Our operations are split into two divisions, Kelvoro Inspection Services and Kelvoro Engineering services.</p>
  <p>We pick the best talent from the industry and have heavily invested in our developing our staff skills further through regular rigorous external and internal training to keep up with the industry trends.</p>
</div>
<a class="abs btn" style="left:673px;top:1644px;width:166px;height:51px">LEARN MORE</a>

<!-- inspection -->
<h2 class="abs h2 center" style="left:0;width:1200px;top:1830px">Inspection</h2>
<div class="abs" style="left:308px;top:1891px;width:584px;height:358px;background:radial-gradient(ellipse at center,#8d9096,#b9bbbf 55%,#fff 80%)" role="img" aria-label="Illustration of a storage tank on a concrete base with an inspection device"></div>
<svg class="abs chev" style="left:196px;top:2079px" viewBox="0 0 26 44"><polyline points="22,2 4,22 22,42" fill="none" stroke="#555" stroke-width="1.5"/></svg>
<svg class="abs chev" style="left:966px;top:2079px" viewBox="0 0 26 44"><polyline points="4,2 22,22 4,42" fill="none" stroke="#555" stroke-width="1.5"/></svg>
<div class="abs insp-title center">STORAGE TANK INSPECTION – API 653<br>&amp; EEMUA 159</div>
<p class="abs insp-copy center">Our Inspection team has the technical capability, backed by the right equipment to provide full range solutions in accordance with the client's requirement, and in compliance with local and international standards. We offer the following inspection services</p>
<a class="abs btn" style="left:516px;top:2459px;width:168px;height:51px">LEARN MORE</a>

<!-- blog -->
<div class="abs blog-kicker">Latest Update</div>
<h2 class="abs blog-title">Latest Bog</h2>
<div class="abs" style="left:77px;top:2775px;width:141px;height:116px;border:4px solid #4a5890;background:linear-gradient(135deg,#2a2f38,#6a7078 50%,#c8d040)" role="img" aria-label="Technician inspecting a turbine"></div>
<div class="abs post-date">18-Feb-2020</div>
<div class="abs post-title">Lorem Ipsum is Simply dummy<br>Text of the Printing</div>
<p class="abs post-copy">Lorem Ipsum is simply dummy text of the printing and typesetting industry. Lorem Ipsum has been the industry's standard dummy text ever since the .</p>
<div class="abs round fill" style="left:234px;top:2976px"><svg width="14" height="22" viewBox="0 0 14 22"><polyline points="11,2 3,11 11,20" fill="none" stroke="#fff" stroke-width="2"/></svg></div>
<div class="abs round line" style="left:288px;top:2976px"><svg width="14" height="22" viewBox="0 0 14 22"><polyline points="3,2 11,11 3,20" fill="none" stroke="var(--red)" stroke-width="2"/></svg></div>
<div class="abs" style="left:707px;top:2686px;width:416px;height:311px;background:linear-gradient(135deg,#5a7fb0,#8a96a0 45%,#7a5a40 70%,#4a3a30)" role="img" aria-label="Technician taking an ultrasonic reading on a wet steel plate"></div>

<!-- footer -->
<div class="abs brand" style="left:108px;top:3210px;font-size:28px"><span class="dot"></span>Kelvoro Tek</div>
<a class="abs social" style="left:144px;top:3317px" aria-label="Social page one"></a>
<a class="abs social" style="left:198px;top:3317px" aria-label="Social page two"></a>

<div class="abs f-head" style="left:346px;top:3138px">SITEMAP</div>
<ul class="abs sitemap" style="left:344px;top:3183px">
  <li>Home</li><li>About Us</li><li>Inspection</li><li>NDT Services</li><li>Advance NDT Services</li><li>Engineering Services</li><li>Contact Us</li>
</ul>

<div class="abs f-head" style="left:612px;top:3138px">CONTACT US</div>
<div class="abs contact-row" style="left:612px;top:3179px">
  <svg width="18" height="26" viewBox="0 0 18 26"><path d="M9 1C4.6 1 1 4.6 1 9c0 6 8 16 8 16s8-10 8-16c0-4.4-3.6-8-8-8z" fill="var(--red)"/><circle cx="9" cy="9" r="3.2" fill="#fff"/></svg>
  <div>Harbour Rd, Block 4<br>P.O. BOX 40021-80100<br>Mombasa Kenya</div>
</div>
<div class="abs contact-row" style="left:610px;top:3274px">
  <svg width="20" height="20" viewBox="0 0 24 24"><path d="M6.6 10.8c1.4 2.8 3.8 5.1 6.6 6.6l2.2-2.2c.3-.3.7-.4 1-.2 1.1.4 2.3.6 3.6.6.6 0 1 .4 1 1V20c0 .6-.4 1-1 1C10.6 21 3 13.4 3 4c0-.6.4-1 1-1h3.5c.6 0 1 .4 1 1 0 1.3.2 2.5.6 3.6.1.3 0 .7-.2 1z" fill="var(--red)"/></svg>
  <div>+ 254 20 555 0142/3</div>
</div>
<div class="abs contact-row" style="left:610px;top:3322px">
  <svg width="24" height="18" viewBox="0 0 24 18"><rect x="0" y="0" width="24" height="18" rx="2" fill="var(--red)"/><polyline points="1,2 12,10 23,2" fill="none" stroke="#fff" stroke-width="2"/></svg>
  <div>info@kelvoro-tek.com</div>
</div>

<div class="abs f-head" style="left:879px;top:3138px">NEWSLETTER</div>
<p class="abs news-copy" style="left:879px;top:3180px">Would you like to receive our exclusive update for signup !</p>
<div class="abs email-field" style="left:878px;top:3244px;width:245px;height:52px">Enter Email *</div>
<a class="abs btn" style="left:877px;top:3302px;width:246px;height:51px;font-weight:400">SUBSCRIBE</a>

<div class="abs rule"></div>
<div class="abs copyright center">©Kelvoro-tek -2020 All Rights Reserved.</div>

</body>
</html>
```